Harborline Energy - needs a business card

Harborline Energy is a U.S. based diesel sourcing and distribution company that supports American oil & gas fields through providing quality product and consistent services.

Target Market(s)

Oil and Gas

Contact Information for Business Card

The background of the card must be white to ensure the logo pops.

Font styles to use
Serif
Sans Serif

Colors

Designer to choose colors to be used in the design.

Requirements
Must have
• Front of Card: Tag line: Harborline Energy, Powering America's Oil & Gas fields.
• Not sure if you guys do this part but just in case...
• Dale Menschow
• Owner/CEO
• C:555.318.4076
• E:Dmenschow@harborlineenergy.example
• W:Harborlineenergy.example
• Locations: Servicing the Powder River, DJ basin and Bakken formations.
• Back of Card: " Frac fueling is what we do. We understand how important diesel fuel is to your operation, which is why our main service line is Frac fueling. We assure our supply and stand by our service"

```html
<!DOCTYPE html>
<html lang="en">
<head>
<meta charset="utf-8">
<title>Harborline Energy – Business Card</title>
<link href="https://fonts.googleapis.com/css2?family=EB+Garamond:wght@700;800&family=Arimo:wght@400&display=swap" rel="stylesheet">
<style>
  :root {
    --navy: #0a2483;
    --red: #d10f16;
    --white: #ffffff;
    --rule-grey: #e6e6e6;
    --card-bg: #ffffff;
  }
  * { margin: 0; padding: 0; box-sizing: border-box; }
  html, body { width: 1037px; height: 1200px; overflow: hidden; background: var(--card-bg); }
  .card { position: relative; width: 1037px; height: 1200px; background: var(--card-bg); font-family: "EB Garamond", Georgia, serif; }

  /* Front */
  .banner { position: absolute; left: 88px; top: 18px; width: 868px; height: 142px; }
  .banner-ends { position: absolute; inset: 0; }
  .banner-panel { position: absolute; left: 73px; top: 0; width: 721px; height: 142px; background: var(--navy); text-align: center; color: var(--white); }
  .banner-title { font-weight: 800; font-size: 52px; letter-spacing: 0.5px; line-height: 1; margin-top: 36px; }
  .banner-tagline { font-family: "Arimo", Arial, sans-serif; font-size: 19px; margin-top: 12px; }

  .role-line { position: absolute; left: 270px; top: 194px; font-weight: 700; font-size: 38px; color: var(--navy); white-space: nowrap; }
  .role-line .role { color: var(--red); margin-right: 10px; }

  .brand-mark { position: absolute; left: 25px; top: 260px; width: 335px; height: 290px; display: flex; flex-direction: column; align-items: center; justify-content: center; gap: 14px; color: var(--navy); }
  .brand-mark .dot { width: 120px; height: 120px; border-radius: 50%; background: var(--navy); }
  .brand-mark .brand-name { font-weight: 800; font-size: 40px; line-height: 1.05; text-align: center; }

  .contact-list { position: absolute; left: 395px; top: 262px; list-style: none; color: var(--navy); font-weight: 700; }
  .contact-list li { display: flex; align-items: center; height: 50px; font-size: 34px; white-space: nowrap; }
  .contact-list li.email { font-size: 29px; }
  .contact-list svg { width: 34px; height: 34px; margin-right: 14px; flex: none; }

  .front-rule { position: absolute; left: 0; top: 570px; width: 1037px; height: 23px; background: var(--navy); border-radius: 0 0 10px 10px; }

  /* Back */
  .service-statement { position: absolute; left: 60px; top: 676px; width: 920px; font-family: "Arimo", Arial, sans-serif; font-size: 27.5px; line-height: 36px; color: var(--navy); text-align: center; }

  .brand-mark.back { left: 330px; top: 820px; width: 380px; height: 340px; }
  .brand-mark.back .dot { width: 150px; height: 150px; }
  .brand-mark.back .brand-name { font-size: 48px; }

  .back-rule { position: absolute; left: 0; top: 1174px; width: 1037px; height: 24px; background: var(--navy); border-radius: 10px 10px 0 0; }
</style>
</head>
<body>
<div class="card">
  <header class="banner">
    <svg class="banner-ends" viewBox="0 0 868 142" aria-hidden="true">
      <path d="M0 0 H58 Q84 71 58 142 H0 Q26 71 0 0Z" fill="#d10f16"/>
      <path d="M38 0 H54 Q80 71 54 142 H38 Q64 71 38 0Z" fill="#e6e6e6"/>
      <path d="M868 0 H810 Q784 71 810 142 H868 Q842 71 868 0Z" fill="#d10f16"/>
      <path d="M830 0 H814 Q788 71 814 142 H830 Q804 71 830 0Z" fill="#e6e6e6"/>
    </svg>
    <div class="banner-panel">
      <div class="banner-title">HARBORLINE ENERGY</div>
      <div class="banner-tagline">Harborline Energy, Powering America's Oil &amp; Gas fields.</div>
    </div>
  </header>

  <div class="role-line"><span class="role">OWNER/CEO</span>DALE MENSCHOW</div>

  <div class="brand-mark">
    <span class="dot"></span>
    <span class="brand-name">HARBORLINE<br>ENERGY</span>
  </div>

  <ul class="contact-list">
    <li><svg viewBox="0 0 24 24"><path d="M6.6 10.8a15 15 0 0 0 6.6 6.6l2.2-2.2c.3-.3.7-.4 1-.2 1.1.4 2.3.6 3.6.6.6 0 1 .4 1 1V20c0 .6-.4 1-1 1A17 17 0 0 1 3 4c0-.6.4-1 1-1h3.5c.6 0 1 .4 1 1 0 1.3.2 2.5.6 3.6.1.3 0 .7-.2 1z" fill="#d10f16"/></svg>555.318.4076</li>
    <li class="email"><svg viewBox="0 0 24 24" fill="none" stroke="#d10f16" stroke-width="1.8"><rect x="2" y="5" width="20" height="14"/><path d="M2 5l10 8 10-8M2 19l7-7M22 19l-7-7"/></svg>Dmenschow@harborlineenergy.example</li>
    <li><svg viewBox="0 0 24 24" fill="none" stroke="#d10f16" stroke-width="1.6"><circle cx="12" cy="12" r="9"/><path d="M3 12h18M12 3c3 3 3 15 0 18M12 3c-3 3-3 15 0 18M5 7.5h14M5 16.5h14"/></svg>Harborlineenergy.example</li>
    <li><svg viewBox="0 0 24 24" fill="none" stroke="#d10f16" stroke-width="1.6"><path d="M12 22s7-7 7-12a7 7 0 0 0-14 0c0 5 7 12 7 12z"/><circle cx="12" cy="10" r="2.6"/></svg>Servicing the Powder River</li>
    <li><svg viewBox="0 0 24 24" fill="none" stroke="#d10f16" stroke-width="1.6"><path d="M12 22s7-7 7-12a7 7 0 0 0-14 0c0 5 7 12 7 12z"/><circle cx="12" cy="10" r="2.6"/></svg>DJ basin</li>
    <li><svg viewBox="0 0 24 24" fill="none" stroke="#d10f16" stroke-width="1.6"><path d="M12 22s7-7 7-12a7 7 0 0 0-14 0c0 5 7 12 7 12z"/><circle cx="12" cy="10" r="2.6"/></svg>Bakken formations</li>
  </ul>

  <div class="front-rule"></div>

  <p class="service-statement">Frac fueling is what we do. We understand how important diesel fuel is to your operation,which is why our main service line is Frac fueling. We assure our supply and stand by our service</p>

  <div class="brand-mark back">
    <span class="dot"></span>
    <span class="brand-name">HARBORLINE<br>ENERGY</span>
  </div>

  <div class="back-rule"></div>
</div>
</body>
</html>
```